Business Card Design

Take existing logo/brand and develop business card for sales team.
We have two separate brands and require a business card for each.

1. VoxHarbor
2. MyNimbusLinko

Refer to our websites www.voxharbor.example.au and www.mynimbuslinko.example.au for designs currently implemented and in the marketplace.

Both cards are brands of our parent company Quorra Systems Pty Ltd - an Australian Telecommunications company in the medium business sector. We have only business customers, no retail/residential consumers.

Target Market(s)

Australian Business - small to medium enterprise

Industry/Entity Type

Business

Contact Information for Business Card

Lev Dorrit
Sales Director
Mobile: +61 400 555 187
Direct: +61 3 9555 0137
Email: lev@voxharbor.example.au
VoxHarbor (a brand of Quorra Systems Pty Ltd)

Lev Dorrit
Sales Director
Mobile: +61 400 555 187
Direct: +61 3 9555 0137
Email: lev@mynimbuslinko.example.au
MyNimbusLinko (a brand of Quorra Systems Pty Ltd)

Font styles to use
Sans Serif
Other font styles liked:
• Roboto Condensed, Open Sans

Requirements
Must have
• Clean lines, crisp fonts - suggest Roboto Condensed or similar.
• Must be easy to read and clear.
• Brand colour #0C8CCD
• Two colour maximum
Nice to have
• Modern, intellectual and unique design.
Should not have
• No die cuts
• No copies or rip-offs of other designs

```html
<!DOCTYPE html>
<html lang="en">
<head>
<meta charset="utf-8">
<title>MyNimbusLinko Business Card</title>
<link rel="stylesheet" href="https://fonts.googleapis.com/css2?family=Open+Sans:wght@400;600;700&display=swap">
<style>
  :root {
    --brand: #0C8CCD;
    --ink: #3d3d3f;
    --muted: #555558;
    --paper: #ffffff;
    --backdrop: #e4e4e6;
  }
  * { box-sizing: border-box; margin: 0; padding: 0; }
  html, body {
    width: 1200px; height: 768px; overflow: hidden;
    background: var(--backdrop);
    font-family: "Open Sans", Arial, sans-serif;
    color: var(--ink);
  }
  .canvas {
    position: relative; width: 1200px; height: 768px;
  }
  .card {
    position: absolute; top: 219px;
    width: 540px; height: 330px;
    background: var(--paper);
    box-shadow: 0 6px 18px rgba(0,0,0,0.18);
    overflow: hidden;
  }
  .card--front { left: 40px; }
  .card--back { left: 620px; }

  .edge-band {
    position: absolute; left: 0; bottom: 0;
    width: 540px; height: 22px; display: block;
  }
  .edge-band .band-brand { fill: var(--brand); }
  .edge-band .band-ink { fill: var(--ink); }

  /* front */
  .wordmark {
    display: flex; align-items: center; gap: 10px;
    font-weight: 400; color: var(--ink);
  }
  .wordmark__square {
    background: var(--brand); flex: none;
  }
  .card--front .wordmark {
    position: absolute; left: 60px; top: 126px;
    font-size: 46px; letter-spacing: -0.5px;
  }
  .card--front .wordmark__square { width: 52px; height: 52px; }

  /* back */
  .brand-block {
    position: absolute; left: 34px; top: 78px;
    width: 148px; height: 148px;
    background: var(--brand);
  }
  .brand-lockup {
    position: absolute; right: 26px; top: 34px;
    text-align: right;
  }
  .card--back .wordmark {
    font-size: 22px; justify-content: flex-end; gap: 6px;
  }
  .card--back .wordmark__square { width: 22px; height: 22px; }
  .brand-lockup__tagline {
    font-size: 8.5px; color: var(--muted); margin-top: 1px;
  }
  .person {
    position: absolute; left: 250px; top: 104px;
  }
  .person__name {
    font-size: 19px; font-weight: 700; color: var(--brand);
  }
  .person__role {
    font-size: 12px; color: var(--muted); margin-top: 1px;
  }
  .contacts {
    position: absolute; left: 250px; top: 186px;
    list-style: none; font-size: 13.5px; color: var(--ink);
  }
  .contacts li {
    display: flex; align-items: center; gap: 10px; height: 21px;
  }
  .contacts svg { width: 12px; height: 12px; fill: var(--brand); flex: none; }
  .contacts .accent { color: var(--brand); }
</style>
</head>
<body>
<main class="canvas">

  <section class="card card--front" aria-label="Business card front">
    <div class="wordmark">
      <span class="wordmark__square"></span>
      <span class="wordmark__name">MyNimbusLinko</span>
    </div>
    <svg class="edge-band" viewBox="0 0 540 22" aria-hidden="true">
      <polygon class="band-brand" points="0,10 352,14 360,22 0,22"/>
      <polygon class="band-ink" points="346,12 540,8 540,22 356,22"/>
    </svg>
  </section>

  <section class="card card--back" aria-label="Business card back">
    <div class="brand-block"></div>

    <div class="brand-lockup">
      <div class="wordmark">
        <span class="wordmark__square"></span>
        <span class="wordmark__name">MyNimbusLinko</span>
      </div>
      <p class="brand-lockup__tagline">a brand of Quorra Systems Pty Ltd</p>
    </div>

    <div class="person">
      <p class="person__name">Lev Dorrit</p>
      <p class="person__role">Sales Director</p>
    </div>

    <ul class="contacts">
      <li>
        <svg viewBox="0 0 12 12" aria-hidden="true"><path d="M3 0h6a1 1 0 0 1 1 1v10a1 1 0 0 1-1 1H3a1 1 0 0 1-1-1V1a1 1 0 0 1 1-1zm0 1.5v7.5h6V1.5zM6 9.8a.7.7 0 1 0 0 1.4.7.7 0 0 0 0-1.4z"/></svg>
        <span>+61 400 555 187</span>
      </li>
      <li>
        <svg viewBox="0 0 12 12" aria-hidden="true"><path d="M1 3c0-1 1-1.6 5-1.6S11 2 11 3v1.2H8.6V3.2H3.4v1H1zM2.5 5h7l1 6h-9zM6 6.4a1.6 1.6 0 1 0 0 3.2 1.6 1.6 0 0 0 0-3.2z"/></svg>
        <span>+61 3 9555 0137</span>
      </li>
      <li>
        <svg viewBox="0 0 12 12" aria-hidden="true"><path d="M0 2h12v1L6 7 0 3zm0 2.2 6 4 6-4V10H0z"/></svg>
        <span>lev@mynimbuslinko.example.au</span>
      </li>
      <li>
        <svg viewBox="0 0 12 12" aria-hidden="true"><path d="M6 0a6 6 0 1 0 0 12A6 6 0 0 0 6 0zm-.6 1.3v2.2H3.3c.4-1.1 1.2-2 2.1-2.2zm1.2 0c.9.2 1.7 1.1 2.1 2.2H6.6zM1.4 4.7h1.7a9 9 0 0 0 0 2.6H1.4a4.7 4.7 0 0 1 0-2.6zm2.9 0h1.1v2.6H4.3a8 8 0 0 1 0-2.6zm2.3 0h1.1a8 8 0 0 1 0 2.6H6.6zm2.3 0h1.7a4.7 4.7 0 0 1 0 2.6H8.9a9 9 0 0 0 0-2.6zM3.3 8.5h2.1v2.2c-.9-.2-1.7-1.1-2.1-2.2zm3.3 0h2.1c-.4 1.1-1.2 2-2.1 2.2z"/></svg>
        <span>www.<span class="accent">mynimbuslinko</span>.example.au</span>
      </li>
    </ul>

    <svg class="edge-band" viewBox="0 0 540 22" aria-hidden="true">
      <polygon class="band-brand" points="0,10 352,14 360,22 0,22"/>
      <polygon class="band-ink" points="346,12 540,8 540,22 356,22"/>
    </svg>
  </section>

</main>
</body>
</html>
```